Billboard for RV Park

I am looking for a new billboard design for our RV park. The dimensions are 10' tall x 40' long. It will be illuminated at night and printed on vinyl.
To give you an idea of our park, you can look at our website at http://www.mesaquailcamp.com/
The things I want on the sign are:
-Exit Now (In large letters)
-Mention of the sagebrush diner
-"Wifi and Cable"
-"Large Pull though sites"
-Wayfarer Club logo (I have two options attached)
I have also attached what our other billboard looks like. The new one does not need to look anything like it, but I thought I'd show an example. The new billboard is bigger, so it has room for more info on it.
I don't have any specific ideas on the design, but I would like it to be eye catching.

```html
<!DOCTYPE html>
<html lang="en">
<head>
<meta charset="utf-8">
<title>Mesa Quail Camp RV Park Billboard</title>
<link rel="stylesheet" href="https://fonts.googleapis.com/css2?family=Anton&family=Archivo+Black&family=Passion+One:wght@700&display=swap">
<style>
  :root {
    --backdrop: #e4e8ed;
    --frame: #ffffff;
    --panel-top: #0c0c0e;
    --panel-bottom: #3a3b40;
    --maroon: #7b1f26;
    --yellow: #f6e600;
    --white: #ffffff;
    --exit-bg: #050505;
    --exit-edge: #c9c9c9;
  }
  * { margin: 0; padding: 0; box-sizing: border-box; }
  html, body {
    width: 1200px; height: 498px; overflow: hidden;
    background: var(--backdrop);
  }
  .billboard {
    position: absolute; left: 33px; top: 103px;
    width: 1134px; height: 292px;
    border: 6px solid var(--frame);
    background: linear-gradient(180deg, var(--panel-top) 0%, #1d1e22 45%, var(--panel-bottom) 100%);
    overflow: hidden;
  }
  .scene-band {
    position: absolute; left: 0; bottom: 0; width: 100%; height: 110px;
    background: linear-gradient(90deg, #5c6a3a 0%, #7d6f52 14%, #6b5a8a 38%, #2fb8c9 60%, #34c3d0 80%, #4e8a6c 100%);
    opacity: 0.85;
  }
  .brand {
    position: absolute; left: 26px; top: 22px;
    display: flex; align-items: center; gap: 14px;
  }
  .brand-mark {
    width: 70px; height: 70px; border-radius: 50%;
    background: var(--maroon);
  }
  .brand-name {
    font-family: "Anton", sans-serif;
    font-size: 40px; line-height: 1.02; color: var(--white);
    letter-spacing: 1px; text-transform: uppercase;
  }
  .outlined {
    font-family: "Passion One", sans-serif; font-weight: 700;
    color: var(--maroon); text-transform: uppercase;
    -webkit-text-stroke: 1.5px var(--white);
    paint-order: stroke fill;
    text-shadow: 0 0 3px var(--white), 0 0 2px var(--white);
    position: absolute;
  }
  .conjunction { left: 164px; top: 132px; font-size: 34px; letter-spacing: 1px; }
  .diner-name { left: 22px; top: 168px; font-size: 52px; letter-spacing: 1px; }
  .amenities {
    position: absolute; left: 464px; top: 20px;
    font-family: "Archivo Black", sans-serif; font-size: 24px;
    color: var(--yellow); letter-spacing: 0.5px; white-space: nowrap;
  }
  .gallery { position: absolute; top: 58px; left: 436px; height: 142px; }
  .photo {
    position: absolute; top: 0; height: 142px;
    border: 2px solid var(--white);
  }
  .photo-sites { left: 0; width: 168px; background: linear-gradient(180deg, #cfe3f1 0%, #a9bf8c 55%, #b9b2a2 100%); }
  .photo-diner { left: 180px; width: 142px; background: linear-gradient(180deg, #efe6cf 0%, #d8c08a 55%, #7a4e2e 100%); }
  .photo-pool { left: 333px; width: 148px; background: linear-gradient(180deg, #3e9ae0 0%, #6fb2d6 35%, #16b6d9 60%, #10a8cf 100%); }
  .photo-office { left: 495px; width: 165px; background: linear-gradient(180deg, #9fcdf0 0%, #c8a272 50%, #7a6a48 100%); }
  .exit-now {
    position: absolute; left: 893px; top: 216px;
    width: 224px; height: 62px;
    background: var(--exit-bg);
    border: 2px solid var(--exit-edge);
    border-radius: 4px;
    display: flex; align-items: center; justify-content: center;
    font-family: "Anton", sans-serif; font-size: 46px;
    color: var(--yellow); letter-spacing: 1px;
  }
</style>
</head>
<body>
  <main class="billboard">
    <div class="scene-band" role="img" aria-label="Photo of the park's pool deck and grounds with a tractor at left"></div>

    <div class="brand">
      <div class="brand-mark"></div>
      <div class="brand-name">Mesa Quail Camp<br>RV Park</div>
    </div>

    <div class="outlined conjunction">And</div>
    <div class="outlined diner-name">Sagebrush Diner</div>

    <div class="amenities">LARGE PULL . FREE WIFI AND CABLE</div>

    <div class="gallery">
      <div class="photo photo-sites" role="img" aria-label="Photo of pull-through RV sites with trees"></div>
      <div class="photo photo-diner" role="img" aria-label="Photo of the diner dining room"></div>
      <div class="photo photo-pool" role="img" aria-label="Photo of the swimming pool"></div>
      <div class="photo photo-office" role="img" aria-label="Photo of the park office building"></div>
    </div>

    <div class="exit-now">EXIT NOW</div>
  </main>
</body>
</html>
```